Brochure Design Project The Quiet Willow

Very tight deadline** Please accept only if you can start working as soon as possible**The Quiet Willow is a personal concierge business. I have already used Sketchwharf for a logo and postcards. Thanks! I can send content after you layout the text. Thanks again!<br/>** I also want the front to somehow include the following "Personal Concierge Services - Affordable Rates."

Target Market(s)

working class to affluent

Font styles to use
Serif

Requirements
Must have
• PLEASE SEE BROCHURE PRINTING TEMPLATE. I will send content. The layout must be eye catching and visually appealing. I am looking to send to printer by 3 p.m. EST tomorrow. Please begin designing asap! Thank you!

```html
<!DOCTYPE html>
<html lang="en">
<head>
<meta charset="utf-8">
<title>The Quiet Willow – Brochure</title>
<link href="https://fonts.googleapis.com/css2?family=Lato:ital,wght@0,300;0,400;0,700;1,300&family=Open+Sans:wght@400&display=swap" rel="stylesheet">
<style>
  :root {
    --page-bg: #e6e6e6;
    --paper: #ffffff;
    --brand-red: #d71920;
    --brand-red-dark: #b5121a;
    --ink: #1d1d1d;
    --ink-soft: #3a3a3a;
    --photo-light: #f2f2f2;
    --photo-mid: #9a9a9a;
    --photo-dark: #2b2b2b;
  }
  * { box-sizing: border-box; margin: 0; padding: 0; }
  html, body { width: 1200px; height: 1000px; overflow: hidden; }
  body {
    background: radial-gradient(circle at 50% 45%, #f7f7f7 0%, var(--page-bg) 75%);
    font-family: "Lato", sans-serif;
    color: var(--ink);
    position: relative;
  }

  /* ---------- Inside spread ---------- */
  .inside-spread {
    position: absolute;
    left: 40px; top: 220px;
    width: 780px; height: 560px;
    background: var(--paper);
    box-shadow: 0 10px 28px rgba(0,0,0,.18);
    overflow: hidden;
  }
  .spread-panel {
    position: absolute; top: 0; width: 260px; height: 100%;
    border-right: 1px solid rgba(0,0,0,.06);
    z-index: 2;
  }
  .spread-panel:nth-child(1) { left: 0; }
  .spread-panel:nth-child(2) { left: 260px; }
  .spread-panel:nth-child(3) { left: 520px; border-right: none; }
  .panel-copy {
    position: absolute; left: 20px; right: 20px;
    font-family: "Open Sans", sans-serif;
    font-size: 9.6px; line-height: 13.5px;
    text-align: justify; color: var(--ink-soft);
  }
  .spread-panel:nth-child(1) .panel-copy { top: 66px; }
  .spread-panel:nth-child(2) .panel-copy { top: 38px; }
  .spread-panel:nth-child(3) .panel-copy { top: 14px; }

  .spread-band {
    position: absolute; left: 0; top: 0;
    width: 780px; height: 560px;
    z-index: 1;
  }
  .spread-photo {
    position: absolute; left: 0; right: 0; bottom: 0; height: 200px;
    background: linear-gradient(90deg, var(--photo-light) 0%, var(--photo-mid) 20%, var(--photo-dark) 45%, var(--photo-mid) 70%, var(--photo-light) 100%);
    clip-path: polygon(0 46%, 100% 0, 100% 100%, 0 100%);
    opacity: .85;
    z-index: 1;
  }

  /* ---------- Front cover ---------- */
  .front-cover {
    position: absolute;
    left: 870px; top: 200px;
    width: 280px; height: 600px;
    background: var(--paper);
    box-shadow: 0 10px 28px rgba(0,0,0,.22);
    overflow: hidden;
  }
  .cover-heading {
    position: absolute; top: 46px; left: 0; right: 0;
    text-align: center; line-height: 1.1;
  }
  .cover-heading .kicker {
    display: block; font-weight: 300; font-size: 23px;
    letter-spacing: .5px; color: var(--ink);
  }
  .cover-heading .title {
    display: block; font-weight: 700; font-size: 23px; color: var(--ink);
  }
  .cover-heading .rates {
    display: block; margin-top: 8px;
    font-weight: 300; font-style: italic; font-size: 15px;
    letter-spacing: 1px; color: var(--ink-soft);
  }
  .cover-photo {
    position: absolute; top: 140px; left: 0; right: 0; height: 250px;
    background: linear-gradient(90deg, var(--photo-mid) 0%, var(--photo-dark) 25%, var(--photo-light) 50%, var(--photo-dark) 75%, var(--photo-mid) 100%);
    opacity: .85;
  }
  .cover-band {
    position: absolute; left: 0; bottom: 0;
    width: 280px; height: 240px;
  }
  .cover-name {
    position: absolute; left: 28px; right: 28px; bottom: 78px;
    height: 82px;
    background: var(--paper);
    border-radius: 8px;
    display: flex; align-items: center; justify-content: center; gap: 10px;
  }
  .cover-name .mark {
    width: 12px; height: 12px; background: var(--brand-red);
  }
  .cover-name .name {
    font-family: "Lato", sans-serif; font-weight: 700; font-size: 21px;
    color: var(--brand-red);
  }
</style>
</head>
<body>

  <section class="inside-spread" aria-label="Brochure inside spread">
    <div class="spread-panel">
      <p class="panel-copy">Sed ut perspiciatis unde omnis iste natus error sit voluptatem accusantium doloremque laudantium, totam rem aperiam, eaque ipsa quae ab illo inventore veritatis et quasi architecto beatae vitae dicta sunt explicabo. Nemo enim ipsam voluptatem quia voluptas sit aspernatur aut odit aut fugit, sed quia consequuntur magni dolores eos qui ratione voluptatem sequi nesciunt. Neque porro quisquam est, qui dolorem ipsum quia dolor sit amet, consectetur, adipisci velit, sed quia non numquam eius modi tempora incidunt ut labore et dolore magnam aliquam quaerat voluptatem. Ut enim ad minima veniam, quis nostrum exercitationem ullam corporis suscipit laboriosam, nisi ut aliquid ex ea commodi consequatur? Quis autem vel eum iure reprehenderit qui in ea voluptate velit esse quam nihil molestiae consequatur, vel illum qui dolorem eum fugiat quo voluptas</p>
    </div>
    <div class="spread-panel">
      <p class="panel-copy">Sed ut perspiciatis unde omnis iste natus error sit voluptatem accusantium doloremque laudantium, totam rem aperiam, eaque ipsa quae ab illo inventore veritatis et quasi architecto beatae vitae dicta sunt explicabo. Nemo enim ipsam voluptatem quia voluptas sit aspernatur aut odit aut fugit, sed quia consequuntur magni dolores eos qui ratione voluptatem sequi nesciunt. Neque porro quisquam est, qui dolorem ipsum quia dolor sit amet, consectetur, adipisci velit, sed quia non numquam eius modi tempora incidunt ut labore et dolore magnam aliquam quaerat voluptatem. Ut enim ad minima veniam, quis nostrum exercitationem ullam corporis suscipit laboriosam, nisi ut aliquid ex ea commodi consequatur? Quis autem vel eum iure reprehenderit qui in ea voluptate velit esse quam nihil molestiae consequatur, vel illum qui dolorem eum fugiat quo voluptas</p>
    </div>
    <div class="spread-panel">
      <p class="panel-copy">Sed ut perspiciatis unde omnis iste natus error sit voluptatem accusantium doloremque laudantium, totam rem aperiam, eaque ipsa quae ab illo inventore veritatis et quasi architecto beatae vitae dicta sunt explicabo. Nemo enim ipsam voluptatem quia voluptas sit aspernatur aut odit aut fugit, sed quia consequuntur magni dolores eos qui ratione voluptatem sequi nesciunt. Neque porro quisquam est, qui dolorem ipsum quia dolor sit amet, consectetur, adipisci velit, sed quia non numquam eius modi tempora incidunt ut labore et dolore magnam aliquam quaerat voluptatem. Ut enim ad minima veniam, quis nostrum exercitationem ullam corporis suscipit laboriosam, nisi ut aliquid ex ea commodi consequatur? Quis autem vel eum iure reprehenderit qui in ea voluptate velit esse quam nihil molestiae consequatur, vel illum qui dolorem eum fugiat quo voluptas</p>
    </div>

    <svg class="spread-band" viewBox="0 0 780 560" aria-hidden="true">
      <polygon points="0,400 780,300 780,352 0,452" fill="var(--brand-red)"/>
      <polygon points="0,452 780,352 780,358 0,458" fill="var(--brand-red-dark)"/>
    </svg>
    <div class="spread-photo" role="img" aria-label="Photo of a line-up of concierge staff in uniforms: waiters, a chauffeur, a doorman, a valet and a chef"></div>
  </section>

  <section class="front-cover" aria-label="Brochure front cover">
    <h1 class="cover-heading">
      <span class="kicker">PERSONAL</span>
      <span class="title">Concierge Services</span>
      <span class="rates">Affordable Rates</span>
    </h1>
    <div class="cover-photo" role="img" aria-label="Photo of a chauffeur, a waiter holding a tray with wine glasses and a doorman standing side by side"></div>
    <svg class="cover-band" viewBox="0 0 280 240" aria-hidden="true">
      <polygon points="0,30 280,0 280,240 0,240" fill="var(--brand-red)"/>
    </svg>
    <div class="cover-name">
      <span class="mark"></span>
      <span class="name">The Quiet Willow</span>
    </div>
  </section>

</body>
</html>
```